PowerPoint Template Design

We are an independent private equity and advisory firm (mergers and acquisitions), based in Brazil. We are looking for a power point template to use for companies presentations to investors and other targets (ie competitors).
Find attached the actual template that we use, we need something with this structure but more customized.

- Cover slide with our logo, project name and current date
- Index/Agenda slide
- Content slides
a. Slide with title, subtitle, text and footer. The footer should contain the page number, the person who we are sending to and the word "CONFIDENTIAL"
b. Slide with title, subtitle, text and pictures/charters/graphics
- Final slide with adress and contacts

We do not want something very colorful, we need something plain, simple but modern.

Target Market(s)

Investors, CEOs, CFOs, other advisory firms like DNTallis, DSRH, Almsbury, etc.

Industry/Entity Type

Equity

Requirements
Must have
• - the same colors used by our designer;
- one font only (Century Gothic);

```html
<!DOCTYPE html>
<html lang="en">
<head>
<meta charset="UTF-8">
<title>Presentation Title Here</title>
<link href="https://fonts.googleapis.com/css2?family=Didact+Gothic&family=Questrial&family=Carlito:wght@700&display=swap" rel="stylesheet">
<style>
  :root {
    --page-bg: #ffffff;
    --header-tint: #f1f1f1;
    --rule: #dcdcdc;
    --title-ink: #666666;
    --body-ink: #4a4a4a;
    --lead-ink: #333333;
    --bullet-fill: #3c3c3c;
    --footer-tint: #efefef;
    --brand-ink: #5a5a5a;
  }
  html, body {
    margin: 0;
    padding: 0;
    width: 1200px;
    height: 900px;
    overflow: hidden;
    background: var(--page-bg);
  }
  .slide {
    position: relative;
    width: 1200px;
    height: 900px;
    background: var(--page-bg);
    font-family: "Didact Gothic", "Questrial", sans-serif;
  }
  .slide-header {
    position: absolute;
    left: 0; top: 0;
    width: 1200px;
    height: 108px;
    border-bottom: 1px solid var(--rule);
    box-sizing: border-box;
  }
  .header-texture {
    position: absolute;
    left: 0; top: 0;
    width: 700px;
    height: 107px;
    background: linear-gradient(90deg, var(--header-tint) 0%, #f7f7f7 55%, rgba(255,255,255,0) 100%);
  }
  .slide-title {
    position: absolute;
    left: 42px;
    top: 34px;
    margin: 0;
    font-family: "Questrial", "Didact Gothic", sans-serif;
    font-weight: 400;
    font-size: 40px;
    line-height: 1;
    color: var(--title-ink);
    letter-spacing: 0.5px;
  }
  .point-list {
    position: absolute;
    left: 36px;
    top: 180px;
    width: 1074px;
    margin: 0;
    padding: 0;
    list-style: none;
  }
  .point {
    position: relative;
    padding-left: 45px;
    margin-bottom: 39px;
    font-size: 21px;
    line-height: 39px;
    color: var(--body-ink);
    text-align: justify;
  }
  .point-marker {
    position: absolute;
    left: 0;
    top: 8px;
    width: 24px;
    height: 24px;
  }
  .point-lead {
    color: var(--lead-ink);
    font-weight: 700;
    -webkit-text-stroke: 0.4px var(--lead-ink);
  }
  .slide-footer {
    position: absolute;
    left: 0; bottom: 0;
    width: 1200px;
    height: 58px;
    border-top: 1px solid #e6e6e6;
    background: linear-gradient(180deg, #fafafa 0%, var(--footer-tint) 100%);
  }
  .page-number {
    position: absolute;
    left: 36px;
    top: 17px;
    font-family: "Carlito", sans-serif;
    font-weight: 700;
    font-size: 21px;
    color: var(--lead-ink);
  }
  .brand-name {
    position: absolute;
    right: 27px;
    top: 10px;
    font-family: "Didact Gothic", sans-serif;
    font-size: 36px;
    line-height: 1;
    letter-spacing: 14px;
    margin-right: -14px;
    color: var(--brand-ink);
  }
</style>
</head>
<body>
<div class="slide">
  <header class="slide-header">
    <div class="header-texture" role="img" aria-label="Soft grey dotted texture band"></div>
    <h1 class="slide-title">Persentation Title Here</h1>
  </header>

  <ul class="point-list">
    <li class="point">
      <svg class="point-marker" viewBox="0 0 24 24" aria-hidden="true"><circle cx="12" cy="12" r="11" fill="var(--bullet-fill)"/><path d="M10 7.5 L14.5 12 L10 16.5" fill="none" stroke="#fff" stroke-width="2.6" stroke-linecap="round" stroke-linejoin="round"/></svg>
      <span class="point-lead">Lorem ipsum dolor sit ipsum</span> Lorem ipsum dolor sit ipsum Lorem ipsum Lorem ipsum dolor sit ipsum Lorem ipsum dolor sit ipsum Lorem ipsum.
    </li>
    <li class="point">
      <svg class="point-marker" viewBox="0 0 24 24" aria-hidden="true"><circle cx="12" cy="12" r="11" fill="var(--bullet-fill)"/><path d="M10 7.5 L14.5 12 L10 16.5" fill="none" stroke="#fff" stroke-width="2.6" stroke-linecap="round" stroke-linejoin="round"/></svg>
      <span class="point-lead">Lorem ipsum dolor sit</span> ipsum Lorem ipsum dolor sit ipsum Lorem ipsum Lorem ipsum dolor sit ipsum Lorem ipsum dolor sit ipsum Lorem ipsum.
    </li>
    <li class="point">
      <svg class="point-marker" viewBox="0 0 24 24" aria-hidden="true"><circle cx="12" cy="12" r="11" fill="var(--bullet-fill)"/><path d="M10 7.5 L14.5 12 L10 16.5" fill="none" stroke="#fff" stroke-width="2.6" stroke-linecap="round" stroke-linejoin="round"/></svg>
      Lorem ipsum dolor sit ipsum Lorem ipsum dolor sit ipsum Lorem ipsum Lorem ipsum dolor sit ipsum Lorem ipsum dolor sit ipsum Lorem ipsum.
    </li>
    <li class="point">
      <svg class="point-marker" viewBox="0 0 24 24" aria-hidden="true"><circle cx="12" cy="12" r="11" fill="var(--bullet-fill)"/><path d="M10 7.5 L14.5 12 L10 16.5" fill="none" stroke="#fff" stroke-width="2.6" stroke-linecap="round" stroke-linejoin="round"/></svg>
      <span class="point-lead">Lorem ipsum dolor sit ipsum</span> Lorem ipsum dolor sit ipsum Lorem ipsum Lorem ipsum dolor sit ipsum Lorem ipsum dolor sit ipsum Lorem ipsum.
    </li>
    <li class="point">
      <svg class="point-marker" viewBox="0 0 24 24" aria-hidden="true"><circle cx="12" cy="12" r="11" fill="var(--bullet-fill)"/><path d="M10 7.5 L14.5 12 L10 16.5" fill="none" stroke="#fff" stroke-width="2.6" stroke-linecap="round" stroke-linejoin="round"/></svg>
      <span class="point-lead">Lorem ipsum dolor sit</span> ipsum Lorem ipsum dolor sit ipsum Lorem ipsum Lorem ipsum dolor sit ipsum Lorem ipsum dolor sit ipsum Lorem ipsum.
    </li>
  </ul>

  <footer class="slide-footer">
    <span class="page-number">Page : 04</span>
    <span class="brand-name">VANTRO</span>
  </footer>
</div>
</body>
</html>
```